Clear sticker design for packaging

I need 4” diameter clear stickers designed for birthdays, thank you , teachers day and all the other special days to complete my gift packaging. They will go on the top of each tube to differentiate each gift for each occasion. Our design is on craft paper and I’ve uploaded a few examples of what we are trying to achieve. Last picture is the top of our tube where the stickers will be placed. We don’t want too much color unless for Christmas and Valentine’s Day maybe! We are working with black and gold or a mixture of both mostly

```html
<!DOCTYPE html>
<html lang="en">
<head>
<meta charset="utf-8">
<title>Occasion Stickers – Black &amp; Gold Set</title>
<link rel="stylesheet" href="https://fonts.googleapis.com/css2?family=Montserrat:wght@500;600&family=Libre+Bodoni:wght@400&family=Great+Vibes&family=Yellowtail&display=swap">
<style>
  :root {
    --kraft: #d9b98a;
    --kraft-light: #e4c89e;
    --kraft-dark: #c9a673;
    --ink: #111111;
    --gold-light: #f6ec86;
    --gold-mid: #e8b52c;
    --gold-deep: #c98f12;
    --cut-line: #2a2218;
  }
  html, body {
    margin: 0;
    padding: 0;
    width: 1200px;
    height: 1200px;
    overflow: hidden;
    background: var(--kraft);
  }
  .sheet {
    display: block;
    width: 1200px;
    height: 1200px;
  }
  .label-small {
    font-family: "Montserrat", sans-serif;
    font-weight: 600;
    letter-spacing: 2.5px;
    fill: var(--ink);
  }
  .label-tagline {
    font-family: "Montserrat", sans-serif;
    font-weight: 500;
    font-size: 14px;
    fill: var(--ink);
  }
  .label-serif {
    font-family: "Libre Bodoni", serif;
    font-size: 56px;
    fill: var(--ink);
  }
  .label-script {
    font-family: "Yellowtail", cursive;
    fill: var(--ink);
  }
  .label-script-fine {
    font-family: "Great Vibes", cursive;
    font-size: 70px;
    fill: var(--ink);
  }
  .gold-word {
    fill: url(#goldFoil);
    stroke: var(--ink);
    stroke-width: 5px;
    paint-order: stroke;
    stroke-linejoin: round;
  }
  .gold-small {
    fill: url(#goldFoil);
    stroke: var(--ink);
    stroke-width: 1.4px;
    paint-order: stroke;
  }
  .cut-line {
    fill: none;
    stroke: var(--cut-line);
    stroke-width: 0.8;
  }
  .frame-ring {
    fill: none;
    stroke: var(--ink);
    stroke-width: 3.2;
  }
  .burst-area { fill: var(--ink); opacity: 0.05; }
  .sprig-area { fill: var(--ink); }
</style>
</head>
<body>
<svg class="sheet" viewBox="0 0 1200 1200" xmlns="http://www.w3.org/2000/svg">
  <defs>
    <radialGradient id="kraftTone" cx="50%" cy="45%" r="75%">
      <stop offset="0" stop-color="var(--kraft-light)"/>
      <stop offset="0.7" stop-color="var(--kraft)"/>
      <stop offset="1" stop-color="var(--kraft-dark)"/>
    </radialGradient>
    <linearGradient id="goldFoil" x1="0" y1="0" x2="1" y2="1">
      <stop offset="0" stop-color="var(--gold-light)"/>
      <stop offset="0.45" stop-color="var(--gold-mid)"/>
      <stop offset="0.7" stop-color="var(--gold-deep)"/>
      <stop offset="1" stop-color="var(--gold-light)"/>
    </linearGradient>
    <linearGradient id="goldSplash" x1="0.9" y1="0" x2="0.2" y2="1">
      <stop offset="0" stop-color="#f5f08a"/>
      <stop offset="0.45" stop-color="#e9b62e"/>
      <stop offset="0.7" stop-color="#dba31c"/>
      <stop offset="1" stop-color="#f7d54a"/>
    </linearGradient>
  </defs>

  <rect class="kraft-background" width="1200" height="1200" fill="url(#kraftTone)"/>

  <!-- Birthday, black -->
  <g class="sticker sticker--birthday-black">
    <circle class="cut-line" cx="364" cy="232" r="174"/>
    <circle class="burst-area" cx="364" cy="232" r="150" role="img" aria-label="Radiating sunburst lines and sparkles"/>
    <text class="label-small" x="327" y="193" font-size="20" text-anchor="middle">HAPPY</text>
    <text class="label-script" x="364" y="284" font-size="100" text-anchor="middle" textLength="296" lengthAdjust="spacingAndGlyphs">Birthday</text>
  </g>

  <!-- Birthday, gold -->
  <g class="sticker sticker--birthday-gold">
    <circle class="cut-line" cx="836" cy="232" r="174"/>
    <circle class="burst-area" cx="836" cy="232" r="150" role="img" aria-label="Radiating sunburst lines and sparkles"/>
    <text class="label-small gold-small" x="799" y="193" font-size="20" text-anchor="middle">HAPPY</text>
    <text class="label-script gold-word" x="836" y="284" font-size="100" text-anchor="middle" textLength="296" lengthAdjust="spacingAndGlyphs">Birthday</text>
  </g>

  <!-- Thank you, black -->
  <g class="sticker sticker--thanks-black">
    <circle class="cut-line" cx="364" cy="599" r="174"/>
    <circle class="frame-ring" cx="364" cy="599" r="150"/>
    <text class="label-serif" x="364" y="576" text-anchor="middle" textLength="232" lengthAdjust="spacingAndGlyphs">THANK</text>
    <text class="label-script-fine" x="368" y="628" text-anchor="middle" textLength="116" lengthAdjust="spacingAndGlyphs">You</text>
    <text class="label-tagline" x="364" y="672" text-anchor="middle">For Making</text>
    <text class="label-tagline" x="364" y="691" text-anchor="middle">Our Day Special</text>
  </g>

  <!-- Thank you, gold -->
  <g class="sticker sticker--thanks-gold">
    <circle class="cut-line" cx="836" cy="599" r="174"/>
    <circle class="frame-ring" cx="836" cy="599" r="150"/>
    <path role="img" aria-label="Gold foil splash" fill="url(#goldSplash)"
      d="M786 481 C812 472 840 474 862 480 C900 490 936 520 946 560 C956 600 950 640 930 672 C910 704 874 722 836 724 C796 726 758 712 734 684 C712 658 708 620 714 584 C720 540 748 496 786 481 Z"/>
    <text class="label-serif" x="836" y="576" text-anchor="middle" textLength="232" lengthAdjust="spacingAndGlyphs">THANK</text>
    <text class="label-script-fine" x="840" y="628" text-anchor="middle" textLength="116" lengthAdjust="spacingAndGlyphs">You</text>
    <text class="label-tagline" x="836" y="672" text-anchor="middle">For Making</text>
    <text class="label-tagline" x="836" y="691" text-anchor="middle">Our Day Special</text>
  </g>

  <!-- Teacher's Day, black -->
  <g class="sticker sticker--teachers-black">
    <circle class="cut-line" cx="364" cy="967" r="174"/>
    <rect class="sprig-area" x="296" y="834" width="142" height="18" rx="9" role="img" aria-label="Leafy branch ornament"/>
    <text class="label-small" x="342" y="911" font-size="22" text-anchor="middle">HAPPY</text>
    <text class="label-script" x="360" y="996" font-size="92" text-anchor="middle" textLength="286" lengthAdjust="spacingAndGlyphs">Teacher´s</text>
    <text class="label-small" x="385" y="1050" font-size="22" text-anchor="middle" letter-spacing="6">DAY</text>
    <rect class="sprig-area" x="292" y="1086" width="142" height="18" rx="9" role="img" aria-label="Leafy branch ornament"/>
  </g>

  <!-- Teacher's Day, gold -->
  <g class="sticker sticker--teachers-gold">
    <circle class="cut-line" cx="836" cy="967" r="174"/>
    <rect class="sprig-area" x="768" y="834" width="142" height="18" rx="9" role="img" aria-label="Leafy branch ornament"/>
    <text class="label-small" x="814" y="911" font-size="22" text-anchor="middle">HAPPY</text>
    <text class="label-script gold-word" x="832" y="996" font-size="92" text-anchor="middle" textLength="286" lengthAdjust="spacingAndGlyphs">Teacher´s</text>
    <text class="label-small" x="857" y="1050" font-size="22" text-anchor="middle" letter-spacing="6">DAY</text>
    <rect class="sprig-area" x="764" y="1086" width="142" height="18" rx="9" role="img" aria-label="Leafy branch ornament"/>
  </g>
</svg>
</body>
</html>
```